Hair & Skin Product Line

I need someone to design clear product labels that can go on pink bottles. I'm looking for someone who can add graphics such as avocado and honey to the label as these are ingredients in our products. The colors we want incorporated are gold, blue, white and purple. I will upload information about our company identity and information on one label. Whoever we choose, we will use them to create 11 more labels.

Target Market(s)

Woman 25-50, Natural, straight or curly hair.

Industry/Entity Type

Beauty

```html
<!DOCTYPE html>
<html lang="en">
<head>
<meta charset="utf-8">
<title>Avocado &amp; Honey Moisture Repair Shampoo – Label</title>
<link href="https://fonts.googleapis.com/css2?family=Federo&family=Montserrat:wght@500;600&family=Oswald:wght@500&display=swap" rel="stylesheet">
<style>
  :root {
    --label-pink: #f1b3c5;
    --label-pink-light: #f7c9d6;
    --label-pink-deep: #e49fb4;
    --white: #ffffff;
    --gold-dark: #b8894a;
    --gold-light: #ecd3a0;
    --blue: #a9d4ec;
    --purple: #8e3f7d;
    --honey: #f2a62a;
    --honey-light: #f9cf6a;
    --avocado: #7fa55a;
  }
  * { margin: 0; padding: 0; box-sizing: border-box; }
  html, body { width: 1200px; height: 1197px; overflow: hidden; }
  body {
    background: linear-gradient(90deg, var(--label-pink-deep) 0%, var(--label-pink-light) 22%, var(--label-pink) 55%, var(--label-pink-light) 85%, var(--label-pink-deep) 100%);
    font-family: "Montserrat", sans-serif;
    position: relative;
  }
  .label { position: absolute; inset: 0; }
  .brand {
    position: absolute; top: 110px; left: 0; right: 0;
    display: flex; align-items: center; justify-content: center; gap: 18px;
    color: var(--white); font-family: "Montserrat", sans-serif;
    font-weight: 500; font-size: 58px; letter-spacing: 1px;
  }
  .brand-dot { width: 22px; height: 22px; border-radius: 50%; background: var(--white); }
  .product-name {
    position: absolute; top: 265px; left: 0; right: 0; text-align: center;
    font-family: "Federo", sans-serif; color: var(--white);
    font-size: 150px; line-height: 0.98; text-shadow: 3px 4px 0 rgba(190, 110, 140, 0.45);
  }
  .benefit {
    position: absolute; top: 565px; left: 50%; transform: translateX(-50%);
    padding: 10px 26px; font-weight: 600; font-size: 44px; color: var(--white);
    background: linear-gradient(90deg, var(--gold-dark), var(--gold-light) 50%, var(--gold-dark));
    letter-spacing: 1px; white-space: nowrap;
  }
  .product-type {
    position: absolute; top: 650px; left: 50%; transform: translateX(-50%);
    padding: 6px 26px; font-weight: 600; font-size: 42px; color: var(--white);
    background: var(--blue); border-radius: 4px; letter-spacing: 1px;
  }
  .description {
    position: absolute; top: 745px; left: 0; right: 0; text-align: center;
    color: var(--purple); font-weight: 500; font-size: 33px; line-height: 1.45;
  }
  .divider {
    position: absolute; top: 905px; left: 550px; width: 100px; height: 4px; background: var(--white);
  }
  .ingredient-art {
    position: absolute; top: 935px; left: 290px; width: 650px; height: 200px;
    border-radius: 50% 50% 20% 20%;
    background: radial-gradient(ellipse at 50% 55%, var(--avocado) 0%, var(--honey) 40%, var(--honey-light) 65%, rgba(249, 207, 106, 0) 78%);
  }
  .motto {
    position: absolute; top: 960px; left: 80px;
    transform-origin: left top; transform: rotate(-90deg) translateX(-170px);
    color: var(--white); font-style: italic; font-weight: 600; font-size: 17px; line-height: 1.3;
    text-transform: uppercase;
  }
  .volume {
    position: absolute; top: 1145px; left: 0; right: 0; text-align: center;
    font-family: "Oswald", sans-serif; font-weight: 500; font-size: 34px; letter-spacing: 3px;
    color: var(--white);
  }
</style>
</head>
<body>
  <main class="label">
    <div class="brand"><span class="brand-name">Velvet Root Co</span><span class="brand-dot"></span></div>
    <h1 class="product-name">AVOCADO<br>&amp;HONEY</h1>
    <div class="benefit">MOISTURE REPAIR</div>
    <div class="product-type">SHAMPOO</div>
    <p class="description">Infused w/Biotin + Rosemary<br>Gently cleanses and hydrates for<br>retention, moisture and softness</p>
    <div class="divider"></div>
    <div class="ingredient-art" role="img" aria-label="Illustration of a halved avocado with a honey dipper and golden honey splash"></div>
    <p class="motto">Your only limit is the<br>one you set for yourself!</p>
    <p class="volume">300 ML /10 FL OZ</p>
  </main>
</body>
</html>
```